Business cards to launch an education platform

Hi,
I am looking at having new business cards designed.
I am a startup, developing a web platform for schools and university, the education world. It's an online assessment system.
I would like a card that looks classy, and that is using the colors and the font of my logo.

I have attached:
1) my logo
2) A business card that I have designed quickly so you can have all the information required in the card, but I really don't like it.
3) The font that I am using (Lato Regular) to design my web platform
4) Some screenshots of my web platform so you can have a look at the style that I have.

Target Market(s)

Major market: Education system: Schools and university
Minor markets: Business in general

Industry/Entity Type

Business

Contact Information for Business Card

Lydia Marsh
Director

M: 0437 681 902
E: lydia.marsh@copperLeafSystems.com.au

Requirements
Must have
• The colors of my logo

```html
<!DOCTYPE html>
<html lang="en">
<head>
<meta charset="utf-8">
<title>Copper Leaf Systems – Business Card</title>
<link rel="stylesheet" href="https://fonts.googleapis.com/css2?family=Lato:wght@400;700&family=Open+Sans:wght@400&family=Roboto+Condensed:wght@400&display=swap">
<style>
  :root {
    --backdrop: #a4a5a6;
    --card-light: #eceded;
    --navy: #0b3562;
    --brand-navy: #123f73;
    --accent-blue: #2b9fd8;
    --ink: #3f4145;
    --rule: #4a4c50;
    --soft-white: #dfe3e8;
  }
  * { margin: 0; padding: 0; box-sizing: border-box; }
  html, body {
    width: 1105px;
    height: 1200px;
    overflow: hidden;
    background: var(--backdrop);
  }
  .canvas { position: relative; width: 1105px; height: 1200px; }

  .card {
    position: absolute;
    left: 182px;
    width: 747px;
    height: 425px;
  }
  .card--front { top: 119px; background: var(--card-light); }
  .card--back { top: 637px; background: var(--navy); }

  /* Front: brand block */
  .brand-mark {
    position: absolute;
    left: 600px;
    top: 40px;
    width: 76px;
    height: 76px;
    background: var(--brand-navy);
  }
  .brand-name {
    position: absolute;
    right: 49px;
    top: 150px;
    text-align: right;
    font-family: "Lato", sans-serif;
    font-weight: 400;
    font-size: 29px;
    line-height: 32px;
    letter-spacing: 2px;
    color: var(--brand-navy);
  }

  /* Front: person */
  .person-name {
    position: absolute;
    left: 43px;
    top: 212px;
    font-family: "Roboto Condensed", sans-serif;
    font-size: 37px;
    color: var(--accent-blue);
    line-height: 44px;
  }
  .person-role {
    position: absolute;
    left: 43px;
    top: 258px;
    font-family: "Roboto Condensed", sans-serif;
    font-size: 25px;
    color: var(--ink);
    line-height: 30px;
  }
  .role-rule {
    position: absolute;
    left: 135px;
    top: 277px;
    width: 563px;
    height: 1.5px;
    background: var(--rule);
  }

  /* Front: contacts */
  .contact-list {
    position: absolute;
    left: 43px;
    top: 302px;
    list-style: none;
  }
  .contact-item {
    display: flex;
    align-items: center;
    height: 29px;
    font-family: "Open Sans", sans-serif;
    font-size: 19px;
    color: var(--ink);
  }
  .contact-icon {
    width: 18px;
    height: 18px;
    margin-right: 14px;
    flex: none;
  }

  /* Back */
  .back-name {
    position: absolute;
    left: 0;
    right: 0;
    top: 170px;
    text-align: center;
    font-family: "Lato", sans-serif;
    font-weight: 400;
    font-size: 40px;
    letter-spacing: 3px;
    color: var(--soft-white);
  }
  .back-url {
    position: absolute;
    left: 0;
    right: 0;
    top: 356px;
    text-align: center;
    font-family: "Open Sans", sans-serif;
    font-size: 20px;
    letter-spacing: 0.3px;
    color: var(--soft-white);
  }
</style>
</head>
<body>
<main class="canvas">

  <section class="card card--front">
    <div class="brand-mark"></div>
    <div class="brand-name">COPPER LEAF<br>SYSTEMS</div>

    <h1 class="person-name">Lydia Marsh</h1>
    <p class="person-role">Director</p>
    <div class="role-rule"></div>

    <ul class="contact-list">
      <li class="contact-item">
        <svg class="contact-icon" viewBox="0 0 18 18" aria-hidden="true">
          <rect x="4" y="1" width="10" height="16" rx="2" fill="none" stroke="#2b9fd8" stroke-width="2"/>
          <rect x="7" y="13" width="4" height="1.6" fill="#2b9fd8"/>
        </svg>
        0437 681 902
      </li>
      <li class="contact-item">
        <svg class="contact-icon" viewBox="0 0 18 18" aria-hidden="true">
          <rect x="1" y="4" width="16" height="11" fill="#2b9fd8"/>
          <polyline points="1,4 9,10.5 17,4" fill="none" stroke="#eceded" stroke-width="1.5"/>
        </svg>
        lydia.marsh@copperLeafSystems.com.au
      </li>
      <li class="contact-item">
        <svg class="contact-icon" viewBox="0 0 18 18" aria-hidden="true">
          <circle cx="9" cy="9" r="8" fill="#2b9fd8"/>
          <path d="M5 6 Q8 5 9 8 Q8 11 6 12 M11 4 Q13 7 12 9 Q14 12 13 14" fill="none" stroke="#eceded" stroke-width="1.3"/>
        </svg>
        www.copperLeafSystems.com.au
      </li>
    </ul>
  </section>

  <section class="card card--back">
    <div class="back-name">COPPER LEAF SYSTEMS</div>
    <p class="back-url">www.copperLeafSystems.com.au</p>
  </section>

</main>
</body>
</html>
```